Party invitation with a difference

I have recently turned 65, and I am holding a party for a number of my friends

I am looking for a stylish party invitation possibly in the guise of a rock concert admission ticket./ poster

promoting my band Blue Kettle who will be playing.at the party. We are a middle of the road covers band

I am turning 65 years so something like 65 and still Rocking ...

The party will run from 7.00pm until 11.00pm

Food platter and drink supplied.

No presents please

Date Saturday 30 June 2018
At Marlow & Pike Restaurant, 317, Fenwick Lane. Clevedon, Auckland 2671

RSVP to dennis.hartwell@plumbox.co.nz

Target Market(s)

I have a guest list

Font styles to use

Colors

Designer to choose colors to be used in the design.

Requirements
Must have
• I will want to email the invitation to my guests as well as be able to print some off .
Nice to have
• The invitation is from Dennis and Marion Hartwell
Should not have
• Not be flowery

```html
<!DOCTYPE html>
<html lang="en">
<head>
<meta charset="utf-8">
<title>Blue Kettle Concert &amp; Party Invitation</title>
<link href="https://fonts.googleapis.com/css2?family=Archivo+Black&family=Oswald:wght@500;600&family=Mr+Dafoe&family=Yellowtail&display=swap" rel="stylesheet">
<style>
  :root {
    --kraft-light: #ddc9a9;
    --kraft-dark: #c9ae88;
    --ink: #161412;
    --rust: #a2231b;
    --frame: #4a433b;
    --page: #ffffff;
  }
  html, body {
    margin: 0;
    padding: 0;
    width: 1200px;
    height: 602px;
    overflow: hidden;
    background: var(--page);
  }
  .ticket {
    position: relative;
    width: 1200px;
    height: 602px;
    overflow: hidden;
  }
  .ticket-shape {
    position: absolute;
    inset: 0;
  }
  .ticket p, .ticket h1, .ticket h2 {
    margin: 0;
    position: absolute;
    white-space: nowrap;
  }
  .tagline {
    top: 8px;
    left: 0;
    width: 1200px;
    text-align: center;
    font-family: "Archivo Black", sans-serif;
    font-size: 38px;
    line-height: 48px;
    letter-spacing: 3px;
    color: var(--rust);
  }
  .party-details {
    top: 58px;
    left: 0;
    width: 1200px;
    text-align: center;
    font-family: "Oswald", sans-serif;
    font-weight: 500;
    font-size: 17px;
    line-height: 22px;
    letter-spacing: 2px;
    color: var(--ink);
  }
  .hosts {
    left: 94px;
    top: 116px;
    font-family: "Archivo Black", sans-serif;
    font-size: 58px;
    line-height: 64px;
    letter-spacing: 1px;
    color: var(--ink);
  }
  .surname {
    left: 40px;
    top: 334px;
    font-family: "Archivo Black", sans-serif;
    font-size: 58px;
    line-height: 58px;
    letter-spacing: 2px;
    color: var(--rust);
    transform: rotate(-16deg);
    transform-origin: left bottom;
  }
  .guitar-art {
    position: absolute;
    left: 112px;
    top: 410px;
    width: 330px;
    height: 58px;
    border-radius: 30px 8px 8px 30px;
    background: linear-gradient(90deg, #1b1815, #3a332c);
    transform: rotate(-18deg);
  }
  .invite-line {
    left: 248px;
    top: 420px;
    font-family: "Yellowtail", cursive;
    font-size: 42px;
    line-height: 48px;
    color: var(--rust);
    transform: rotate(-18deg);
  }
  .band-name {
    left: 512px;
    top: 112px;
    font-family: "Archivo Black", sans-serif;
    font-size: 128px;
    line-height: 186px;
    color: var(--ink);
  }
  .band-name span { display: block; }
  .event-type {
    left: 544px;
    top: 456px;
    font-family: "Oswald", sans-serif;
    font-weight: 600;
    font-size: 46px;
    line-height: 52px;
    letter-spacing: 3px;
    color: var(--rust);
  }
  .date-divider {
    position: absolute;
    left: 966px;
    top: 144px;
    width: 2px;
    height: 320px;
    background: var(--frame);
  }
  .date-numbers {
    left: 976px;
    top: 198px;
    writing-mode: vertical-rl;
    font-family: "Oswald", sans-serif;
    font-weight: 600;
    font-size: 28px;
    line-height: 30px;
    letter-spacing: 2px;
    color: var(--rust);
  }
  .date-day {
    left: 1012px;
    top: 128px;
    writing-mode: vertical-rl;
    font-family: "Mr Dafoe", cursive;
    font-size: 96px;
    line-height: 88px;
    color: var(--ink);
  }
  .venue {
    left: 0;
    top: 520px;
    width: 1200px;
    text-align: center;
    font-family: "Oswald", sans-serif;
    font-weight: 600;
    font-size: 28px;
    line-height: 40px;
    letter-spacing: 1px;
    color: var(--rust);
    text-transform: uppercase;
  }
  .venue-lead { font-size: 20px; }
  .rsvp {
    left: 0;
    top: 562px;
    width: 1200px;
    text-align: center;
    font-family: "Oswald", sans-serif;
    font-weight: 500;
    font-size: 17px;
    line-height: 24px;
    letter-spacing: 2px;
    color: var(--ink);
  }
  .rsvp-label { color: var(--rust); font-weight: 600; }
</style>
</head>
<body>
<main class="ticket">
  <svg class="ticket-shape" width="1200" height="602" viewBox="0 0 1200 602" aria-hidden="true">
    <defs>
      <radialGradient id="paper" cx="50%" cy="45%" r="70%">
        <stop offset="0%" stop-color="#ddc9a9"/>
        <stop offset="100%" stop-color="#c9ae88"/>
      </radialGradient>
      <mask id="ticket-cut">
        <rect width="1200" height="602" fill="#fff"/>
        <g fill="#000">
          <circle cx="0" cy="0" r="42"/><circle cx="1200" cy="0" r="42"/>
          <circle cx="0" cy="602" r="42"/><circle cx="1200" cy="602" r="42"/>
          <circle cx="0" cy="106" r="13"/><circle cx="0" cy="152" r="13"/>
          <circle cx="0" cy="198" r="13"/><circle cx="0" cy="244" r="13"/>
          <circle cx="0" cy="290" r="13"/><circle cx="0" cy="336" r="13"/>
          <circle cx="0" cy="382" r="13"/><circle cx="0" cy="428" r="13"/>
          <circle cx="0" cy="474" r="13"/>
          <circle cx="1200" cy="106" r="13"/><circle cx="1200" cy="152" r="13"/>
          <circle cx="1200" cy="198" r="13"/><circle cx="1200" cy="244" r="13"/>
          <circle cx="1200" cy="290" r="13"/><circle cx="1200" cy="336" r="13"/>
          <circle cx="1200" cy="382" r="13"/><circle cx="1200" cy="428" r="13"/>
          <circle cx="1200" cy="474" r="13"/>
        </g>
      </mask>
    </defs>
    <rect width="1200" height="602" fill="url(#paper)" mask="url(#ticket-cut)"/>
    <rect x="86" y="86" width="1022" height="426" rx="14" fill="none" stroke="#4a433b" stroke-width="1.5"/>
  </svg>

  <p class="tagline">65 AND STILL ROCKING!</p>
  <p class="party-details">7.00PM – 11.00PM &nbsp;·&nbsp; FOOD PLATTERS &amp; DRINKS SUPPLIED &nbsp;·&nbsp; NO PRESENTS PLEASE</p>

  <h1 class="hosts">DENNIS &amp;<br>MARION</h1>
  <p class="surname">HARTWELL</p>

  <div class="guitar-art" role="img" aria-label="Black electric bass guitar illustration"></div>
  <p class="invite-line">Invite you to</p>

  <h2 class="band-name"><span>Blue</span><span>Kettle</span></h2>
  <p class="event-type">CONCERT &amp; PARTY</p>

  <div class="date-divider"></div>
  <p class="date-numbers">30 JUNE 2018</p>
  <p class="date-day">Saturday</p>

  <p class="venue"><span class="venue-lead">at</span> Marlow &amp; Pike Restaurant, 317, Fenwick Lane. Clevedon, Auckland 2671</p>
  <p class="rsvp"><span class="rsvp-label">RSVP</span> dennis.hartwell@plumbox.co.nz</p>
</main>
</body>
</html>
```